Android Shop Depot Listing Screenshot Design

We would like to create new screenshots for our Android app in the Shop Depot to A/B test against the current version.

You can view our current Android Shop Depot listing here: https://shop.trelvani.com/store/apps/details?id=com.quorvix.android&hl=en

Attached I have added screenshots of the app that I would like to be included. Please edit the screenshots to generic text (e.g. John Smith, 123 Main St, etc.).

You can use the same text we have in the current ones. For text for the criminal screenshot please view our iOS Kiosk Hub listing: https://apps.mondrelo.com/us/app/quorvix-background-check/id918274650?mt=8

If you want to come up with new text please feel free to!

I also attached a few examples of other app screenshots that we like.

Android ShopDepot Listing Guidelines: https://help.trelvani.com/trelvanishop/android-developer/answer/5520931?hl=en

Industry/Entity Type

Store

Font styles to use
Sans Serif

Colors
f0f0f0

Requirements
Must have
• ~Generic names and data like "John Smith", "54 Main St. Springfield, NJ 09876"
• ~Screenshot for Person Search, Criminal Records, Phone Search, Email Search, and Property Search. In that order.
• ~Headlines either the ones used in our current screenshots (https://shop.trelvani.com/store/apps/details?id=com.quorvix.android&hl=en) or new ones you come up with.
• ~Must meet Android screenshot guidelines.
• ~Optimized for downloads.
• Must use following color palette:
• Dark purple #3B2469
• Light purple #7E6F9C
• Very dark gray #333333
• Dark gray #666666
• Gray #999999
• Blue gray #CFD9DE
• Green #5CB85C
• Navy #003577
• Yellow #F3B607
• Magenta #F0386B

```html
<!DOCTYPE html>
<html lang="en">
<head>
<meta charset="utf-8">
<title>Email Search – Listing Screenshot</title>
<link rel="stylesheet" href="https://fonts.googleapis.com/css2?family=Montserrat:wght@500;600&family=Roboto:wght@400;500;700&display=swap">
<style>
  :root {
    --dark-purple: #3B2469;
    --purple-bar: #4A3381;
    --light-purple: #7E6F9C;
    --lavender: #8F84B4;
    --very-dark-gray: #333333;
    --dark-gray: #666666;
    --gray: #999999;
    --blue-gray: #CFD9DE;
    --magenta: #F0386B;
    --panel: #f0f0f0;
    --white: #ffffff;
    --device-edge: #9ea2a6;
    --wood-dark: #7a4c2a;
    --wood-light: #b9874f;
  }
  html, body {
    margin: 0;
    padding: 0;
    width: 1200px;
    height: 2581px;
    overflow: hidden;
    background: var(--panel);
  }
  .listing-shot {
    display: block;
    width: 1200px;
    height: 2581px;
  }
  .headline-text {
    font-family: "Montserrat", sans-serif;
    font-weight: 600;
    fill: var(--white);
  }
  .feature-title {
    font-family: "Montserrat", sans-serif;
    font-weight: 500;
    fill: var(--white);
    letter-spacing: 6px;
  }
  .app-text { font-family: "Roboto", sans-serif; }
  .status-text { font-size: 40px; fill: var(--white); }
  .appbar-title { font-size: 50px; font-weight: 500; fill: var(--white); }
  .email-address { font-size: 50px; fill: var(--white); letter-spacing: 1px; }
  .section-title { font-size: 68px; fill: var(--dark-purple); }
  .field-label { font-size: 36px; font-weight: 500; fill: var(--gray); }
  .field-value { font-size: 52px; fill: var(--very-dark-gray); }
  .tab-label { font-size: 38px; fill: var(--dark-gray); letter-spacing: 2px; }
  .empty-title { font-size: 40px; font-weight: 700; fill: var(--very-dark-gray); }
  .empty-body { font-size: 32px; fill: var(--gray); }
  .next-section { font-size: 58px; fill: var(--dark-purple); }
  .side-screen-text { font-size: 40px; fill: var(--very-dark-gray); }
</style>
</head>
<body>
<svg class="listing-shot" viewBox="0 0 1200 2581" xmlns="http://www.w3.org/2000/svg">
  <defs>
    <linearGradient id="woodTone" x1="0" y1="0" x2="1" y2="1">
      <stop offset="0" stop-color="var(--wood-light)"/>
      <stop offset="0.5" stop-color="var(--wood-dark)"/>
      <stop offset="1" stop-color="var(--wood-light)"/>
    </linearGradient>
    <linearGradient id="deviceShell" x1="0" y1="0" x2="1" y2="0">
      <stop offset="0" stop-color="#e4e6e8"/>
      <stop offset="1" stop-color="#b4b8bc"/>
    </linearGradient>
    <clipPath id="mainScreen">
      <rect x="406" y="591" width="794" height="1772"/>
    </clipPath>
    <clipPath id="sideScreen">
      <rect x="-300" y="590" width="418" height="1640"/>
    </clipPath>
  </defs>

  <!-- desk surface -->
  <rect class="desk-surface" x="0" y="0" width="1200" height="2581" fill="url(#woodTone)" role="img" aria-label="Wooden desk surface"/>

  <!-- notebook and pen on the desk -->
  <rect class="desk-notebook" x="0" y="2200" width="1120" height="381" fill="#eceae6" role="img" aria-label="Notebook and silver pen lying on the desk"/>

  <!-- device behind the headline -->
  <rect class="device-back" x="155" y="-200" width="1026" height="551" rx="90" fill="#b9bcbf"/>
  <rect x="200" y="-200" width="936" height="500" rx="60" fill="#a6a9ad"/>

  <!-- headline banner -->
  <g class="headline-banner">
    <rect x="-40" y="-40" width="1166" height="280" rx="28" fill="var(--magenta)"/>
    <text class="headline-text" x="560" y="92" font-size="56" text-anchor="middle">CHECK OUT HIDDEN SOCIAL</text>
    <text class="headline-text" x="560" y="180" font-size="56" text-anchor="middle">AND MEDIA PRTOFILES</text>
  </g>

  <!-- side device (left) -->
  <g class="device-side">
    <rect x="-300" y="480" width="459" height="1980" rx="120" fill="url(#deviceShell)" stroke="var(--device-edge)" stroke-width="4"/>
    <g clip-path="url(#sideScreen)">
      <rect x="-300" y="590" width="418" height="1640" fill="var(--white)"/>
      <rect x="-300" y="609" width="418" height="148" fill="var(--dark-purple)"/>
      <text class="app-text status-text" x="0" y="685">8 PM</text>
      <circle cx="88" cy="711" r="6" fill="var(--white)"/>
      <circle cx="88" cy="733" r="6" fill="var(--white)"/>
      <circle cx="88" cy="755" r="6" fill="var(--white)"/>
      <rect x="-300" y="757" width="418" height="70" fill="var(--lavender)"/>
      <text class="app-text" x="0" y="806" font-size="34" fill="var(--white)">BANKRU</text>
      <line x1="-300" y1="940" x2="118" y2="940" stroke="#e3e3e3" stroke-width="3"/>
      <text class="app-text side-screen-text" x="10" y="1122">MMIT</text>
      <line x1="-300" y1="1700" x2="118" y2="1700" stroke="#e3e3e3" stroke-width="3"/>
      <text class="app-text side-screen-text" x="10" y="1890">MMIT</text>
    </g>
  </g>

  <!-- main device -->
  <g class="device-main">
    <rect x="351" y="351" width="1000" height="2400" rx="140" fill="url(#deviceShell)" stroke="var(--device-edge)" stroke-width="4"/>
    <circle cx="560" cy="490" r="18" fill="#4b4f54"/>
    <circle cx="610" cy="490" r="18" fill="#4b4f54"/>
    <rect x="880" y="470" width="200" height="18" rx="9" fill="#8d9196"/>
    <circle cx="1070" cy="430" r="26" fill="#4b4f54"/>

    <g class="app-screen" clip-path="url(#mainScreen)">
      <rect x="406" y="591" width="794" height="1772" fill="var(--white)"/>

      <!-- status bar -->
      <rect x="406" y="591" width="794" height="74" fill="var(--dark-purple)"/>
      <rect x="430" y="610" width="34" height="30" rx="3" fill="none" stroke="var(--white)" stroke-width="3"/>
      <rect x="478" y="610" width="34" height="30" rx="3" fill="none" stroke="var(--white)" stroke-width="3"/>
      <rect x="526" y="610" width="34" height="30" rx="3" fill="none" stroke="var(--white)" stroke-width="3"/>
      <text class="app-text status-text" x="1030" y="645" font-size="36">18%</text>
      <text class="app-text status-text" x="1110" y="645" font-size="36">5:11</text>

      <!-- app bar -->
      <rect x="406" y="665" width="794" height="185" fill="var(--purple-bar)"/>
      <path d="M498 757 H450 M472 733 L448 757 L472 781" fill="none" stroke="var(--white)" stroke-width="6" stroke-linecap="round" stroke-linejoin="round"/>
      <text class="app-text appbar-title" x="578" y="775">Email Report</text>
      <path d="M1100 700 c-22 0 -34 16 -34 36 v26 l-12 16 h92 l-12 -16 v-26 c0 -20 -12 -36 -34 -36 z M1088 786 a12 12 0 0 0 24 0" fill="none" stroke="var(--white)" stroke-width="5"/>

      <!-- email band -->
      <rect x="406" y="850" width="794" height="200" fill="var(--lavender)"/>
      <text class="app-text email-address" x="590" y="905">jcarv412@mailvo.com</text>

      <!-- email icon -->
      <circle cx="905" cy="1110" r="158" fill="var(--white)"/>
      <circle cx="905" cy="1110" r="146" fill="var(--dark-purple)"/>
      <path d="M835 1110 L975 1040 L945 1180 L910 1140 Z" fill="var(--white)"/>
      <path d="M910 1140 L975 1040 L895 1120 Z" fill="#d9d4e6"/>

      <!-- overview -->
      <text class="app-text section-title" x="496" y="1378">Email Overview</text>
      <text class="app-text field-label" x="520" y="1472">OWNER</text>
      <text class="app-text field-value" x="520" y="1534">Jon Carver</text>

      <!-- aliases tab -->
      <rect x="406" y="1555" width="794" height="62" fill="#ececec"/>
      <text class="app-text tab-label" x="975" y="1600" text-anchor="middle">ALIASES</text>

      <!-- empty state card -->
      <rect x="552" y="1645" width="700" height="295" fill="var(--white)" stroke="#dddddd" stroke-width="3"/>
      <path d="M835 1685 h86 a10 10 0 0 1 10 10 v56 a10 10 0 0 1 -10 10 h-46 l-22 20 v-20 h-18 a10 10 0 0 1 -10 -10 v-56 a10 10 0 0 1 10 -10 z" fill="#d6d6d6"/>
      <rect x="874" y="1699" width="8" height="30" fill="var(--white)"/>
      <rect x="874" y="1737" width="8" height="8" fill="var(--white)"/>
      <text class="app-text empty-title" x="878" y="1836" text-anchor="middle">No Aliases Were Found</text>
      <text class="app-text empty-body" x="878" y="1880" text-anchor="middle">We searched for aliases,</text>
      <text class="app-text empty-body" x="878" y="1920" text-anchor="middle">unfortunately we found no data.</text>

      <!-- next section -->
      <rect x="406" y="2180" width="794" height="183" fill="#f6f5f9"/>
      <text class="app-text next-section" x="620" y="2272">Social Media &amp; Web</text>
    </g>

    <!-- home key -->
    <rect x="720" y="2440" width="160" height="56" rx="20" fill="none" stroke="#a8acb0" stroke-width="4"/>
  </g>

  <!-- feature band -->
  <g class="feature-band">
    <rect x="0" y="1950" width="1200" height="228" fill="var(--dark-purple)" fill-opacity="0.86"/>
    <text class="feature-title" x="705" y="2102" font-size="104" text-anchor="middle">EMAIL SEARCH</text>
  </g>
</svg>
</body>
</html>
```